Flyer-Design für Hörgeräteakustik
Ich war top zufrieden! Bereits der erste Flyer war super und nach einer Nachbearbeitung war er perfekt :)
Zielgruppe
Hörgeräteakustik - Die Zielgruppe sind Menschen ab 50 J.
Aufgabenstellung
BILDMATERIAL FOLGT!
Format: Quadrat - Maße noch unentschlossen
Seitenanzahl: 4 Seiten
Falzart: Einbruchfalz
Texte:
Philosophie
Ich möchte Ihr Leben hörbar verbessern
Meine Arbeit als Hörakustik-Meisterin ist für mich nicht nur ein Beruf, sondern auch meine Berufung.
Dank modernster Technik lassen sich unterschiedliche Höreinschränkungen sehr gut ausgleichen. Um gemeinsam die für Sie optimale Hörlösung finden, nehme ich mir Zeit und berate Sie ausführlich und herstellerunabhängig. Mir ist es wichtig, eine Lösung zu finden, die perfekt zu Ihnen und Ihrem Leben passt.
Damit sich Menschen mit eingeschränkter Mobilität professionell von mir beraten und versorgen lassen können, besuche ich sie gerne in ihrer gewohnten Umgebung. Dank einer kleinen Werkstatt in meinem Transporter und der mobilen Messtechnik kann ich alle Leistungen auch bei Ihnen vor Ort erbringen.
Ich vereinbare auch gerne individuelle Termine außerhalb der Ladenöffnungszeiten, sodass einer professionellen Hörsystemversorgung nichts im Wege steht.
Leistungen
-Kostenloser Hörtest
-Hörberatung
-Unverbindliches Probetragen
-Hausbesuch-Service
-Hörgeräte-Fernanpassung
-Angepasster Gehörschutz
Der Weg zum guten Hören
1. Hörtest und Höranalyse
Als ersten Schritt führe ich mit Ihnen einen Hörtest und eine Höranalyse durch. Dabei nehme ich mir Zeit und überprüfe ausführlich Ihr Hörvermögen.
2. Individuelle Hörberatung
Wenn ich bei den Hörmessungen eine Hörminderung feststelle, setzen wir uns zusammen und finden gemeinsam die für Sie optimale Hörlösung. Auf Grundlage Ihrer Wünsche und Bedürfnisse sowie der Ergebnisse der Hörmessung wählen wir dann gemeinsam Probegeräte aus.
3. Individuelle Anpassung
Die von Ihnen ausgewählten Hörgeräte passe ich individuell Ihrem Hörvermögen an.
4. Unverbindliches Probetragen<..

```html
<!DOCTYPE html>
<html lang="de">
<head>
<meta charset="utf-8">
<title>Helena Bramstell Hörakustik – Flyer</title>
<link rel="stylesheet" href="https://fonts.googleapis.com/css2?family=Nunito+Sans:wght@300;400;600;700&family=Dancing+Script:wght@400&display=swap">
<style>
:root{
  --stage:#9b9b9b;
  --paper:#ffffff;
  --slate:#58595b;
  --pink:#d4848f;
  --green:#a9d59b;
  --ink:#4a4a4a;
  --mist:#e0dfdc;
}
*{box-sizing:border-box;margin:0;padding:0}
html,body{width:1200px;height:1200px;overflow:hidden;background:var(--stage)}
body{position:relative;font-family:'Nunito Sans',sans-serif;color:var(--ink)}
.page{position:absolute;width:514px;height:515px;background:var(--paper);overflow:hidden}
.label{position:absolute;color:#fff;font-size:21px;font-weight:400;white-space:nowrap}
.label--left{left:32px;top:370px;transform:rotate(-90deg);transform-origin:left top}
.label--right{left:1146px;top:370px;transform:rotate(-90deg);transform-origin:left top}
.label--bottom{left:0;width:1170px;text-align:center;top:1125px}
.abs{position:absolute}
.script{font-family:'Dancing Script',cursive;color:var(--green)}

/* cover */
.cover{left:72px;top:50px}
.cover__photo{left:0;top:0;width:514px;height:399px;background:radial-gradient(ellipse at 70% 45%,#e6e6e6 0%,#a9a9a9 45%,#6d6d6f 100%)}
.cover__photo-warm{left:0;top:0;width:330px;height:399px;background:linear-gradient(100deg,rgba(186,130,105,.85) 0%,rgba(220,170,145,.7) 40%,rgba(220,170,145,0) 100%)}
.brand{left:300px;top:438px;width:180px;color:var(--pink)}
.brand__name{display:flex;align-items:center;font-size:13px;font-weight:600;line-height:16px;letter-spacing:.4px}
.brand__mark{width:9px;height:9px;border-radius:50%;background:var(--pink);margin-right:7px;flex:none}
.brand__claim{font-size:9.5px;font-weight:400;margin-top:7px;padding-left:16px;color:var(--ink)}

/* back */
.back{left:613px;top:50px;background:var(--slate);color:#fff}
.back__title{left:31px;top:271px;font-size:19px}
.back__intro{left:28px;top:301px;width:150px;text-align:right;font-size:9.4px;font-weight:300;line-height:12.2px;letter-spacing:.1px;color:#e8e8e8}
.back__col{font-size:7.7px;line-height:10.4px;letter-spacing:.1px;color:#fff}
.back__col b{color:var(--pink);font-weight:700}
.back__col small{font-size:6.2px}
.back__col p{margin-bottom:10px}
.back__info{left:185px;top:302px;width:150px}
.back__contact{left:340px;top:303px;width:165px}
.contact-row{display:flex;align-items:center;margin-bottom:2.2px}
.contact-row i{width:8px;height:8px;background:#77787a;margin-right:9px;flex:none}

/* philosophy */
.philo{left:72px;top:590px}
.philo__title{left:185px;top:90px;font-size:15.5px;font-weight:700;color:var(--pink)}
.philo__quote{left:36px;top:116px;width:160px;font-size:23px;line-height:33px;transform:rotate(-9deg)}
.philo__quote span{display:block}
.philo__body{left:185px;top:159px;width:300px;font-size:10.5px;line-height:15.6px;letter-spacing:.35px}
.philo__body p{margin-bottom:15.6px}

/* path */
.path{left:613px;top:590px}
.path__aside{left:339px;top:0;width:175px;height:515px;background:var(--mist)}
.path__photo{left:270px;top:31px;width:213px;height:149px;background:linear-gradient(90deg,#6a4c3e 0%,#c7a792 35%,#efe2d6 70%,#f4ede4 100%)}
.path__title{left:31px;top:28px;font-size:15.5px;font-weight:700;color:var(--green)}
.steps{font-size:8.4px;line-height:12.1px;letter-spacing:.25px}
.steps h3{font-size:8.4px;font-weight:700;color:var(--pink);line-height:12.1px}
.steps p{margin-bottom:11px}
.steps--a{left:31px;top:68px;width:145px}
.steps--b{left:185px;top:150px;width:146px}
.services{left:348px;top:219px}
.services h2{font-size:11.5px;font-weight:600;color:var(--pink);margin-bottom:15px}
.services ul{list-style:none;font-size:10.4px;line-height:15.6px;letter-spacing:.2px;color:var(--pink)}
.services li{position:relative;padding-left:9px}
.services li::before{content:"";position:absolute;left:0;top:6px;width:5px;height:5px;border-radius:50%;background:#fff}
</style>
</head>
<body>

<div class="label label--left">Aussen: Titel</div>
<div class="label label--right">Aussen: Rück</div>
<div class="label label--bottom">Innenseiten</div>

<section class="page cover">
  <div class="abs cover__photo" role="img" aria-label="Foto: Hand hinter dem Ohr lauscht, mit hellen Punkten als Schallwellen"></div>
  <div class="abs cover__photo-warm" aria-hidden="true"></div>
  <div class="abs brand">
    <div class="brand__name"><span class="brand__mark"></span>Helena Bramstell Hörakustik</div>
    <div class="brand__claim">Gut hören, mitten im Leben</div>
  </div>
</section>

<section class="page back">
  <div class="abs script back__title">Ich bin gerne für Sie da</div>
  <p class="abs back__intro">Sie erreichen mich während der Öffnungszeiten in meinem Hör­akustik-Fachgeschäft. Bequem und kostenlos parken können Sie direkt davor.</p>
  <div class="abs back__col back__info">
    <p><b>Helena Bramstell Hörakustik</b><br>Lindenhofweg 14&nbsp;&nbsp;&nbsp; 59480 Wiesenfeld</p>
    <p><b>Öffnungszeiten:</b><br>Mo, Di, Do, Fr 8 – 14 Uhr</p>
    <p>Sehr gerne können wir auch einen per­sönlichen Termin außerhalb dieser Öff­nungszeiten vereinbaren. Dieser kann in meinem Hörakustik-Fachgeschäft oder in Ihrer gewohnten Umgebung stattfinden.</p>
    <p><b>Zusätzliche Zeiten für individuelle Termine</b> <small>(im Fachgeschäft / Hausbesuche):</small><br>Mo, Di, Do, Fr ab 14.30 Uhr<br>Mi ganztags<br>Sa 10 – 16 Uhr</p>
  </div>
  <div class="abs back__col back__contact">
    <p>Nehmen Sie am besten noch heute<br>Kontakt zu mir auf.</p>
    <p>Tel. 02921 4700180<br>Mobil 0157 10203040</p>
    <div class="contact-row"><i></i>info@hoerakustik-bramstell.de</div>
    <div class="contact-row"><i></i>hoerakustik-bramstell.de</div>
    <div class="contact-row"><i></i>Helena Bramstell Hörakustik</div>
    <div class="contact-row"><i></i>helena_bramstell_hoerakustik</div>
  </div>
</section>

<section class="page philo">
  <h2 class="abs philo__title">Philosophie</h2>
  <div class="abs script philo__quote"><span>Ich möchte Ihr</span><span style="padding-left:12px">Leben hörbar</span><span style="padding-left:54px">verbessern</span></div>
  <div class="abs philo__body">
    <p>Meine Arbeit als Hörakustik-Meisterin ist für mich nicht nur ein Beruf, sondern auch meine Berufung.</p>
    <p>Dank modernster Technik lassen sich unterschiedliche Hörein­schränkungen sehr gut ausgleichen. Um gemeinsam die für Sie optimale Hörlösung finden, nehme ich mir Zeit und berate Sie ausführlich und herstellerunabhängig. Mir ist es wichtig, eine Lösung zu finden, die perfekt zu Ihnen und Ihrem Leben passt.</p>
    <p>Damit sich Menschen mit eingeschränkter Mobilität profes­sionell von mir beraten und versorgen lassen können, besu­che ich sie gerne in ihrer gewohnten Umgebung. Dank einer kleinen Werkstatt in meinem Transporter und der mobilen Messtechnik kann ich alle Leistungen auch bei Ihnen vor Ort erbringen.</p>
    <p>Ich vereinbare auch gerne individuelle Termine außerhalb der Ladenöffnungszeiten, sodass einer professionellen Hörsys­temversorgung nichts im Wege steht.</p>
  </div>
</section>

<section class="page path">
  <div class="abs path__aside"></div>
  <div class="abs path__photo" role="img" aria-label="Foto: Akustikerin setzt einer lächelnden Kundin ein Hörgerät ein"></div>
  <h2 class="abs path__title">Der Weg zum guten Hören</h2>
  <div class="abs steps steps--a">
    <h3>1. Hörtest und Höranalyse</h3>
    <p>Als ersten Schritt führe ich mit Ihnen einen Hörtest und eine Hör­analyse durch. Dabei nehme ich mir Zeit und überprüfe ausführlich Ihr Hörvermögen.</p>
    <h3>2. Individuelle Hörberatung</h3>
    <p>Wenn ich bei den Hörmessungen eine Hörminderung feststelle, set­zen wir uns zusammen und finden gemeinsam die für Sie optimale Hörlösung. Auf Grundlage Ihrer Wünsche und Bedürfnisse sowie der Ergebnisse der Hörmessung wählen wir dann gemeinsam Probe­geräte aus.</p>
    <h3>3. Individuelle Anpassung</h3>
    <p>Die von Ihnen ausgewählten Hör­geräte passe ich individuell Ihrem Hörvermögen an.</p>
    <h3>4. Unverbindliches Probetragen</h3>
    <p>Wir vereinbaren eine Probezeit, während der Sie die für Sie ange­passten Hörgeräte unverbindlich in Ihrer gewohnten Hörumgebung tes­ten können. Sollte die erste Anpas­sung der Geräte noch nicht Ihren Vorstellungen entsprechen, justiere ich die vorgenommenen Einstellun­gen gerne nach. Sie können auch gerne verschiedene Hörgeräte tes-</p>
  </div>
  <div class="abs steps steps--b">
    <p style="width:80px">ten, damit Sie die ideale Hörlösung für sich finden.</p>
    <h3>5. Abwicklung mit der Krankenkasse</h3>
    <p>Ich übernehme für Sie die Abwick­lung mit der Krankenkasse – von der Beantragung des Zuschusses über die Dokumentation bis zur Abrechnung. Denn wenn Ihnen Ihr HNO-Arzt ein Hörgerät verordnet hat, erhalten Sie für Ihre Hörgeräte einen Zuschuss.</p>
    <h3>6. Nachsorge und Service</h3>
    <p>Selbstverständlich bin ich auch nach der erfolgreichen Hörgeräte­versorgung für Sie da. Sehr gerne führe ich mindestens einmal im Jahr einen Hörtest durch, um sicherzu­stellen, dass die Einstellungen Ihrer Geräte weiterhin Ihrem Hörbedarf entsprechen. Auch Service-Leistun­gen wie das Reinigen der Hörgerä­te und das Wechseln eines Schall­schlauchs können Sie jederzeit kostenlos in Anspruch nehmen.</p>
  </div>
  <div class="abs services">
    <h2>Leistungen</h2>
    <ul>
      <li>Kostenloser Hörtest</li>
      <li>Hörberatung</li>
      <li>Unverbindliches<br>Probetragen</li>
      <li>Hausbesuch-Service</li>
      <li>Hörgeräte-Fernanpassung</li>
      <li>Angepasster Gehörschutz</li>
    </ul>
  </div>
</section>

</body>
</html>
```